A new company focused on starting and investing in transformative businesses.

We need a simple and clean website with a few pages. we like larkmeadow.com as a starting point. we want the landing page to be very simple with an option to click through on the top right into INVESTOR LOGIN. then we want to be able to scroll down to see more about our company.

Target Market(s)

professional

Coding

Coded - Design and coding required

Number of Pages Required

2 page

Font styles to use
Serif
Sans Serif

Requirements
Must have
• HALVERN BUILDERS logo (attached as a file) on the top with INVESTOR LOGIN as a click through on the right. Please model the click through from larkmeadow.com. The description (also written in attached file) should be on the landing page. we do not want to have to scroll to read the description.

Then we can scroll down to read more about Halvern including the mission and the two types of businesses. More is detailed on the attached file called "Halvern Website Syntax"
Should not have
• should not be slow loading with lots of fancy graphics. should not be busy and with too many colors.

```html
<!DOCTYPE html>
<html lang="en">
<head>
<meta charset="utf-8">
<title>Halvern Builders</title>
<link href="https://fonts.googleapis.com/css2?family=Raleway:wght@300;400;500;600;700&display=swap" rel="stylesheet">
<style>
  :root {
    --ink-dark: #161616;
    --paper: #ffffff;
    --brand-blue: #0a5aa0;
    --link-blue: #2a7fd4;
    --text-body: #3a3a3a;
    --text-heading: #1b1b1b;
    --rule: #c9d7e6;
    --muted-light: #cfcfcf;
  }
  * { box-sizing: border-box; margin: 0; padding: 0; }
  html, body {
    width: 1150px; height: 1200px; overflow: hidden;
    background: var(--paper);
    font-family: "Raleway", Arial, sans-serif;
  }
  .page { position: relative; width: 1150px; height: 1200px; }

  /* Hero */
  .hero-dark {
    position: absolute; left: 0; top: 0; width: 575px; height: 575px;
    background: var(--ink-dark); color: var(--paper);
  }
  .brand {
    position: absolute; left: 91px; top: 30px;
    display: flex; align-items: center; gap: 8px;
  }
  .brand-square { width: 28px; height: 34px; background: var(--brand-blue); }
  .brand-name {
    font-weight: 600; font-size: 13px; letter-spacing: 0.6px; line-height: 15px;
    width: 110px; color: var(--paper);
  }
  .hero-title {
    position: absolute; left: 92px; top: 153px; width: 440px;
    font-size: 28px; line-height: 42px; font-weight: 300;
  }
  .hero-title strong { font-weight: 700; }
  .hero-title .name-mark {
    font-weight: 700;
    text-decoration: underline; text-decoration-color: var(--link-blue);
    text-decoration-thickness: 2px; text-underline-offset: 3px;
  }
  .hero-mission {
    position: absolute; left: 92px; top: 336px; width: 340px;
    font-size: 12px; line-height: 22px; font-weight: 400;
  }
  .scroll-cue {
    position: absolute; left: 528px; top: 423px;
    display: flex; flex-direction: column; align-items: center;
  }
  .scroll-line { width: 1px; height: 47px; background: var(--muted-light); }
  .scroll-text {
    writing-mode: vertical-rl; margin-top: 4px;
    font-size: 9px; letter-spacing: 0.5px; color: var(--muted-light);
  }

  .investor-login {
    position: absolute; left: 991px; top: 32px;
    display: flex; align-items: center; gap: 3px;
    color: var(--brand-blue); text-decoration: none;
    font-size: 12px; font-weight: 500; letter-spacing: 1.2px;
  }
  .hero-feature {
    position: absolute; left: 657px; top: 143px; width: 424px; height: 344px;
    background: linear-gradient(160deg, #2c6fae 0%, #1a5f9f 55%, #175a97 100%);
  }

  /* Business lines */
  .divider {
    position: absolute; left: 575px; top: 658px; width: 1px; height: 346px;
    background: var(--rule);
  }
  .divider-badge {
    position: absolute; left: 539px; top: 795px; width: 72px; height: 72px;
    border-radius: 50%; border: 1px solid var(--rule); background: var(--paper);
    display: flex; align-items: center; justify-content: center;
  }
  .divider-badge span {
    width: 54px; height: 54px; border-radius: 50%; background: var(--brand-blue);
  }
  .business {
    position: absolute; top: 708px; width: 300px;
  }
  .business-ground { left: 173px; }
  .business-special { left: 690px; }
  .business-icon { width: 74px; height: 74px; border-radius: 6px; }
  .icon-growth { background: linear-gradient(135deg, #bfeff0 0%, #f7d88a 100%); }
  .icon-target { background: radial-gradient(circle, #f5b8ba 0%, #e8545c 70%, #f5e6e6 100%); }
  .business-title {
    display: inline-block; margin-top: 29px;
    font-size: 27px; font-weight: 400; color: var(--text-heading);
    line-height: 30px; padding-bottom: 3px;
    border-bottom: 2px solid var(--brand-blue);
  }
  .business-text {
    margin-top: 15px; font-size: 11.6px; line-height: 22px; color: var(--text-body);
  }

  /* Footer */
  .footer {
    position: absolute; left: 0; top: 1089px; width: 1150px; height: 111px;
    background: var(--ink-dark); color: var(--paper); text-align: center;
  }
  .footer-name { margin-top: 27px; font-size: 27px; font-weight: 400; line-height: 32px; }
  .footer-contact { margin-top: 9px; font-size: 12px; }
  .footer-contact a { color: var(--link-blue); text-decoration: none; }
</style>
</head>
<body>
<div class="page">
  <header class="hero-dark">
    <div class="brand">
      <span class="brand-square"></span>
      <span class="brand-name">HALVERN BUILDERS</span>
    </div>
    <h1 class="hero-title"><span class="name-mark">Halvern Builders</span> Is An Entrepreneurial <strong>Firm Focused</strong> On <strong>Building</strong> And <strong>Growing Transformational Companies</strong></h1>
    <p class="hero-mission">Our mission is to build meaningful businesses that create enduring value by impacting people in a measurable way</p>
    <div class="scroll-cue">
      <span class="scroll-line"></span>
      <span class="scroll-text">SCROLL DOWN</span>
    </div>
  </header>

  <a class="investor-login" href="#">INVESTOR LOGIN
    <svg width="14" height="10" viewBox="0 0 14 10" aria-hidden="true"><path d="M0 5h12M8 1l4 4-4 4" fill="none" stroke="currentColor" stroke-width="1.3"/></svg>
  </a>
  <div class="hero-feature" role="img" aria-label="Large brand feature graphic in blue with an architectural photo inside"></div>

  <section>
    <div class="divider"></div>
    <div class="divider-badge"><span></span></div>

    <article class="business business-ground">
      <div class="business-icon icon-growth" role="img" aria-label="Illustration of a magnifying glass over a rising bar chart"></div>
      <h2 class="business-title">Ground Up</h2>
      <p class="business-text">Our ground up business applies a proven analytic process to identify value edge, a form of competitive advantage. We architect transformational companies and are deliberate in creating the foundation necessary to lead an industry.</p>
    </article>

    <article class="business business-special">
      <div class="business-icon icon-target" role="img" aria-label="Illustration of an arrow striking a target"></div>
      <h2 class="business-title">Special Opportunities</h2>
      <p class="business-text">We partner with exceptional teams that create value by transforming lives. Our investment focus includes large companies and spin-outs.</p>
    </article>
  </section>

  <footer class="footer">
    <p class="footer-name">Halvern Builders</p>
    <p class="footer-contact">For media inquiries, please contact <a href="mailto:nora@halvernbuilders.com">nora@halvernbuilders.com</a></p>
  </footer>
</div>
</body>
</html>
```